Tallbridge needs a new rocket based website

We need a new website that will be based on our rocket ship logo. We develop innovative solutions for enterprises. We would like to see a design that when the pages scroll, the rocket launches and goes from launch through a journey, similar to how we approach our customer. We would like areas for "Who are we", "What can we do", "What have we done", "How can we help". http://www.tallbridge.com.au is our current website

Target Market(s)

Government, Enterprise, Cloud

Industry/Entity Type

Software Service

Coding

Coded - Design and coding required

Number of Pages Required

2 page

Requirements
Must have
• We would like to see a design that when the pages scroll, the rocket launches and goes from launch through a journey, similar to how we approach our customer.
• Must have a home page and a detail page.
• Would like to see the logo/rocket animate in some way when you scroll through he page.

```html
<!DOCTYPE html>
<html lang="en">
<head>
<meta charset="utf-8">
<title>Tallbridge — Innovative Software Solutions</title>
<link href="https://fonts.googleapis.com/css2?family=Montserrat:wght@400;500;600;700;800&family=Open+Sans:wght@400;600&display=swap" rel="stylesheet">
<style>
:root{
  --orange:#f58220;
  --orange-dark:#e06d10;
  --ink:#2b2b2b;
  --text:#555;
  --grey-band:#ececec;
  --dark-band:#2d2d2f;
  --footer:#262628;
  --white:#fff;
}
*{box-sizing:border-box;margin:0;padding:0}
html,body{width:1200px;height:3838px;overflow:hidden}
body{font-family:"Open Sans",Arial,sans-serif;color:var(--text);background:var(--white);position:relative}
h1,h2,h3,h4,.nav,.brand{font-family:"Montserrat",Arial,sans-serif}
.section{position:absolute;left:0;width:1200px}

/* header */
.site-header{top:0;height:80px;background:var(--white);border-top:4px solid var(--orange)}
.brand{position:absolute;left:112px;top:20px;display:flex;align-items:center;gap:8px;font-weight:700;font-size:26px;color:var(--orange)}
.brand-dot{width:12px;height:12px;border-radius:50%;background:var(--orange)}
.nav{position:absolute;left:498px;top:32px;display:flex;gap:32px;font-size:15px;font-weight:600;color:var(--ink)}
.header-phone{position:absolute;left:900px;top:30px;font-family:"Montserrat",sans-serif;font-size:16px;font-weight:600;color:var(--orange);display:flex;gap:8px;align-items:center}

/* hero */
.hero{top:80px;height:645px;background:radial-gradient(ellipse at 22% 32%,#c97a2a 0%,#5a3a1d 18%,#1e1a17 45%,#0e0e0e 100%)}
.hero-title{position:absolute;right:113px;top:255px;text-align:right;color:var(--white)}
.hero-title h1{font-size:72px;font-weight:700;letter-spacing:1px;line-height:1}
.hero-title p{font-family:"Montserrat",sans-serif;font-size:30px;font-weight:700;margin-top:6px}
.slider-arrow{position:absolute;top:302px;width:38px;height:38px;border:2px solid #bbb;border-radius:50%}
.slider-arrow.prev{left:24px}.slider-arrow.next{right:24px}
.slider-arrow svg{position:absolute;left:11px;top:10px}

.section-title{font-size:32px;font-weight:500;color:var(--ink);letter-spacing:.5px}
.section-title span{color:var(--orange)}

/* who */
.who{top:725px;height:650px}
.who .section-title{position:absolute;left:112px;top:62px}
.who-text{position:absolute;left:112px;top:110px;width:425px;font-size:13px;line-height:22px}
.btn{position:absolute;left:112px;top:348px;width:128px;height:42px;background:var(--orange);color:var(--white);font-family:"Montserrat",sans-serif;font-weight:600;font-size:14px;display:flex;align-items:center;justify-content:center}
.who-photo{position:absolute;left:600px;top:65px;width:485px;height:338px;background:linear-gradient(135deg,#4b4440,#7f726a 45%,#2f2d2e)}

/* what we do */
.services{top:1375px;height:535px;background:var(--grey-band)}
.services .section-title{position:absolute;left:438px;top:60px;background:var(--grey-band);padding-right:10px}
.service{position:absolute;top:145px;width:260px;text-align:center}
.service-icon{width:136px;height:136px;margin:0 auto;border-radius:50%;background:var(--white);display:flex;align-items:center;justify-content:center}
.service h3{margin-top:22px;font-size:17px;font-weight:600;color:var(--ink);line-height:22px;height:44px}
.service p{margin-top:6px;font-size:12.5px;line-height:20px;padding:0 18px}

/* what done */
.work{top:1910px;height:605px;background:linear-gradient(160deg,#3a3a3c,#232325)}
.work .section-title{position:absolute;left:402px;top:62px;color:var(--white)}
.card{position:absolute;top:145px;width:306px;height:360px;background:var(--white)}
.card-photo{height:190px}
.card h4{margin:18px 24px 0;font-size:17px;font-weight:600;color:var(--orange);line-height:22px}
.card p{margin:14px 24px 0;font-size:12.5px;line-height:20px}

/* help */
.help{top:2515px;height:595px}
.help .section-title{position:absolute;left:450px;top:70px;background:var(--white);padding-right:10px}
.help-intro{position:absolute;left:195px;top:127px;width:810px;text-align:center;font-size:13px;line-height:22px}
.help-circle{position:absolute;top:205px;width:310px;height:310px;border-radius:50%;padding:18px}
.help-circle .inner{width:100%;height:100%;border-radius:50%;background:#151515;display:flex;align-items:center;justify-content:center;text-align:center;color:var(--white);font-family:"Montserrat",sans-serif;font-size:17px;font-weight:500;line-height:24px}

/* map */
.map{top:3110px;height:350px;background:radial-gradient(ellipse at 50% 50%,#efefef 0%,#e4e4e4 60%,#d9d9d9 100%)}
.map-pin{position:absolute;left:578px;top:148px}

/* footer */
.site-footer{top:3460px;height:378px;background:var(--footer);color:#ccc}
.site-footer .brand{top:58px}
.footer-about{position:absolute;left:112px;top:128px;width:230px;font-size:12.5px;line-height:21px}
.footer-col{position:absolute;top:65px}
.footer-col h4{font-size:17px;font-weight:500;color:var(--orange);margin-bottom:28px}
.footer-divider{position:absolute;top:60px;width:1px;height:250px;background:#3c3c3e}
.links li{list-style:none;font-size:12.5px;line-height:25px}
.contact-row{display:flex;gap:22px;font-size:12.5px;line-height:19px;margin-bottom:24px}
.contact-row.email{color:var(--orange)}
.social{display:flex;align-items:center;gap:10px;font-size:16px;color:var(--white)}
.social-square{width:12px;height:12px;background:var(--white)}
.legal{margin-top:48px;font-size:12px;line-height:25px}

.journey{position:absolute;left:0;top:0;width:1200px;height:3838px;pointer-events:none}
</style>
</head>
<body>

<header class="section site-header">
  <div class="brand"><span class="brand-dot"></span>Tallbridge</div>
  <nav class="nav"><span>HOME</span><span>ABOUT</span><span>SERVICES</span><span>CONTACT</span></nav>
  <div class="header-phone">
    <svg width="14" height="14" viewBox="0 0 24 24"><path d="M6.6 10.8a15 15 0 0 0 6.6 6.6l2.2-2.2a1 1 0 0 1 1-.25 11.4 11.4 0 0 0 3.6.57 1 1 0 0 1 1 1V20a1 1 0 0 1-1 1A17 17 0 0 1 3 4a1 1 0 0 1 1-1h3.5a1 1 0 0 1 1 1c0 1.25.2 2.45.57 3.57a1 1 0 0 1-.25 1z" fill="#f58220"/></svg>
    Phone: 1300 555 014
  </div>
</header>

<section class="section hero" role="img" aria-label="Row of glowing light bulbs on a dark background">
  <div class="slider-arrow prev"><svg width="12" height="14" viewBox="0 0 12 14"><path d="M8 2 3 7l5 5" stroke="#ccc" stroke-width="2" fill="none"/></svg></div>
  <div class="slider-arrow next"><svg width="12" height="14" viewBox="0 0 12 14"><path d="M4 2l5 5-5 5" stroke="#ccc" stroke-width="2" fill="none"/></svg></div>
  <div class="hero-title">
    <h1>TALLBRIDGE</h1>
    <p>INNOVATIVE SOFTWARE SOLUTIONS</p>
  </div>
</section>

<section class="section who">
  <h2 class="section-title">WHO <span>ARE WE</span></h2>
  <p class="who-text">Sed ut perspiciatis unde omnis iste natus error sit voluptatem accusantium doloremque laudantium, totam rem aperiam, eaque ipsa quae ab illo inventore veritatis et quasi architecto beatae vitae dicta sunt explicabo. Nemo enim ipsam voluptatem quia voluptas sit aSed ut perspiciatis unde omnis iste natus error sit voluptatem accusantium doloreque laudantium, totam rem aperiam, eaque ipsa quae ab illo inventore veritatis et quasi architecto beatae vitae dicta sunt explicabo. Nemo enim ipsam voluptatem quia voluptas sit aspeSed ut perspiciatis unde omnis iste natus error sit voluptatem accusantium.</p>
  <div class="btn">READ MORE</div>
  <div class="who-photo" role="img" aria-label="Team of developers working together at computer screens"></div>
</section>

<section class="section services">
  <h2 class="section-title">WHAT <span>CAN WE DO</span></h2>
  <div class="service" style="left:82px">
    <div class="service-icon"><svg width="64" height="64" viewBox="0 0 64 64" fill="none" stroke="#f58220" stroke-width="2"><circle cx="34" cy="22" r="12"/><path d="M30 34v6h8v-6M31 44h6M6 44c8 0 12-4 18-4h10M6 52h30l18-12"/></svg></div>
    <h3>E-PARLIAMENT</h3>
    <p>Sed ut perspiciatis unde omnis iste natus error sit voluptatem accusatium doloremque laudantium,s error sitol uptatem accusatit voluptate.</p>
  </div>
  <div class="service" style="left:340px">
    <div class="service-icon"><svg width="64" height="64" viewBox="0 0 64 64" fill="none" stroke="#f58220" stroke-width="2"><path d="M18 38a10 10 0 0 1 2-20 14 14 0 0 1 26 2 9 9 0 0 1 0 18z"/><path d="M24 38v10M32 38v14M40 38v10"/><circle cx="24" cy="50" r="2"/><circle cx="32" cy="54" r="2"/><circle cx="40" cy="50" r="2"/></svg></div>
    <h3>CLOUD</h3>
    <p>Sed ut perspiciatis unde omnis iste natus error sit voluptatem accusatium doloremque laudantium,s error sitol uptatem accusatit voluptate.</p>
  </div>
  <div class="service" style="left:598px">
    <div class="service-icon"><svg width="64" height="64" viewBox="0 0 64 64" fill="none" stroke="#f58220" stroke-width="2"><rect x="10" y="14" width="40" height="38"/><path d="M16 46l30-30 4 4-30 30-6 2z"/><path d="M16 22h12M16 28h8"/></svg></div>
    <h3>ARCHITECTURE<br>AND DESIGN</h3>
    <p>Sed ut perspiciatis unde omnis iste natus error sit voluptatem accusatium doloremque laudantium, tot</p>
  </div>
  <div class="service" style="left:856px">
    <div class="service-icon"><svg width="64" height="64" viewBox="0 0 64 64" fill="none" stroke="#f58220" stroke-width="2"><rect x="8" y="12" width="48" height="40"/><path d="M8 20h48M24 30l-6 6 6 6M40 30l6 6-6 6M35 28l-6 16"/></svg></div>
    <h3>SOFTWARE<br>DEVELOPMENT</h3>
    <p>Sed ut perspiciatis unde omnis iste natus error sit voluptatem accusatium doloremque laudantium, tot</p>
  </div>
</section>

<section class="section work">
  <h2 class="section-title">WHAT <span>HAVE WE DONE</span></h2>
  <article class="card" style="left:112px">
    <div class="card-photo" role="img" aria-label="Hand touching a glowing light bulb" style="background:linear-gradient(135deg,#3a3430,#d89a5c 55%,#4a3a2e)"></div>
    <h4>SED UT PERSPICIATIUDE OMNIS ISTE NAERRO</h4>
    <p>Sed ut perspiciatis unde omnis iste natus rror sit voluptatem accusaium doloremque laudantiums error sitol uptatem</p>
  </article>
  <article class="card" style="left:447px">
    <div class="card-photo" role="img" aria-label="Colleagues reviewing work on a computer" style="background:linear-gradient(135deg,#6f7a84,#c9c4bd 50%,#5d5750)"></div>
    <h4>SED UT PERSPICIATIUDE OMNIS ISTE NAERRO</h4>
    <p>Sed ut perspiciatis unde omnis iste natus rror sit voluptatem accusaium doloremque laudantiums error sitol uptatem</p>
  </article>
  <article class="card" style="left:783px">
    <div class="card-photo" role="img" aria-label="Cloud technology concept held on a tray" style="background:linear-gradient(135deg,#9a9a9a,#e4e4e4 50%,#6c6c6c)"></div>
    <h4>SED UT PERSPICIATIUDE OMNIS ISTE NAERRO</h4>
    <p>Sed ut perspiciatis unde omnis iste natus rror sit voluptatem accusaium doloremque laudantiums error sitol uptatem</p>
  </article>
</section>

<section class="section help">
  <h2 class="section-title">HOW <span>CAN WE HELP</span></h2>
  <p class="help-intro">Sed ut perspiciatis unde omnis iste natus error sit voluptatem accusantium doloremque laudantium, totam rem aperiam, eaque ipsa quaeab illo inventore veritatis et quasi architecto beatae vitae dicta sunt explicabo. Nemo enim ipsam voluptatem quia volu.</p>
  <div class="help-circle" role="img" aria-label="Warm copper toned technology image" style="left:113px;background:linear-gradient(135deg,#e3a56a,#6b3e1c 55%,#c98a4e)"><div class="inner">SED UTPERICIA<br>TIUDEOMNIS LOLOIS</div></div>
  <div class="help-circle" role="img" aria-label="Blue toned technology image" style="left:445px;background:linear-gradient(135deg,#2f4f74,#0f1c2c 55%,#496a8e)"><div class="inner">SED UTPERICIA<br>TIUDEOMNIS LOLOIS</div></div>
  <div class="help-circle" role="img" aria-label="Bronze toned technology image" style="left:777px;background:linear-gradient(135deg,#b5703a,#4a2812 55%,#d08a4c)"><div class="inner">SED UTPERICIA<br>TIUDEOMNIS LOLOIS</div></div>
</section>

<section class="section map" role="img" aria-label="Street map showing the office location">
  <svg class="map-pin" width="44" height="56" viewBox="0 0 44 56"><path d="M22 54S4 34 4 21a18 18 0 0 1 36 0c0 13-18 33-18 33z" fill="#f58220"/><circle cx="22" cy="21" r="7" fill="#fff"/></svg>
</section>

<footer class="section site-footer">
  <div class="brand"><span class="brand-dot"></span>Tallbridge</div>
  <p class="footer-about">Sed ut perspiciatis unde os listenatus errt voluptatem accultum doloremque laudantiuod uperspiciatis unde os iste natus error sited uperspicia vo.</p>
  <div class="footer-divider" style="left:370px"></div>
  <div class="footer-col" style="left:420px">
    <h4>Links</h4>
    <ul class="links"><li>Home</li><li>About</li><li>Clients</li><li>Services</li><li>Contact</li><li>MemberLogin</li></ul>
  </div>
  <div class="footer-divider" style="left:560px"></div>
  <div class="footer-col" style="left:610px">
    <h4>Contact Us</h4>
    <div class="contact-row"><svg width="16" height="20" viewBox="0 0 16 20" fill="none" stroke="#aaa" stroke-width="1.5"><path d="M8 19s6-6.5 6-11A6 6 0 0 0 2 8c0 4.5 6 11 6 11z"/><circle cx="8" cy="8" r="2"/></svg><span>Unit 7, 48 Carrow St<br>Westmere, SA 5071</span></div>
    <div class="contact-row"><svg width="16" height="18" viewBox="0 0 24 24" fill="none" stroke="#aaa" stroke-width="1.5"><path d="M6.6 10.8a15 15 0 0 0 6.6 6.6l2.2-2.2 4.6 1.3V20A17 17 0 0 1 3 4h3.5l1.3 4.6z"/></svg><span>Phone:<br>1300 555 014</span></div>
    <div class="contact-row email"><svg width="18" height="14" viewBox="0 0 18 14" fill="none" stroke="#f58220" stroke-width="1.5"><rect x="1" y="1" width="16" height="12"/><path d="M1 1l8 7 8-7"/></svg><span>Email:<br>info@tallbridge.com.au</span></div>
  </div>
  <div class="footer-divider" style="left:860px"></div>
  <div class="footer-col" style="left:908px">
    <h4>Follow Us</h4>
    <div class="social"><span class="social-square"></span>Newsfeed</div>
    <p class="legal">© 2018 All Rights Are Reserved.<br>Terms of Use | Privacy Policy</p>
  </div>
</footer>

<svg class="journey" viewBox="0 0 1200 3838" aria-hidden="true">
  <defs>
    <g id="journey-marker">
      <circle cx="0" cy="0" r="20" fill="#fff" fill-opacity="0.9" stroke="#f58220" stroke-width="2.5"/>
      <path d="M0 -11 V9 M-7 2 L0 9 L7 2" fill="none" stroke="#f58220" stroke-width="2.5" stroke-linecap="round" stroke-linejoin="round"/>
    </g>
  </defs>
  <g fill="none" stroke="#f58220" stroke-width="2.5" stroke-linecap="round" stroke-dasharray="0.5 7">
    <path d="M598 632 V650 Q598 672 560 672 H120 Q90 672 90 700 V790 Q90 800 104 800"/>
    <path d="M912 1212 V1290 Q912 1320 880 1320 H430 Q400 1320 400 1350 V1440 Q400 1455 425 1455"/>
    <path d="M778 1455 H1120 Q1145 1455 1145 1480 V1752"/>
    <path d="M1145 1792 V1850 Q1145 1880 1115 1880 H390 Q360 1880 360 1910 V1972 Q360 1990 392 1990"/>
    <path d="M930 1990 H1120 Q1145 1990 1145 2015 V2385"/>
    <path d="M1145 2425 V2490 Q1145 2520 1115 2520 H440 Q412 2520 412 2550 V2585 Q412 2600 440 2600"/>
    <path d="M752 2600 H1120 Q1145 2600 1145 2625 V2975"/>
    <path d="M1145 3015 V3080 Q1145 3110 1115 3110 H420"/>
    <path d="M1145 3110 V3628"/>
  </g>
  <use href="#journey-marker" x="598" y="612"/>
  <use href="#journey-marker" x="912" y="1192"/>
  <use href="#journey-marker" x="1145" y="1772"/>
  <use href="#journey-marker" x="1145" y="2405"/>
  <use href="#journey-marker" x="1145" y="2995"/>
  <use href="#journey-marker" x="1145" y="3648"/>
</svg>

</body>
</html>
```